Dorian Valek Photography Business Card

I am a photographer in Philadelphia, PA. I have a business card that I have designed in Photoshop. This has been an ongoing process for me for far too long. I am 85% pleased with what I have. I need some experts like yourself who has that extra 25% to make this card 110%. I use the dots throughout my website as page/topic breaks. I also use the dots on the mailing side of my direct mail pieces.

Bramble Printworks does my printing.
Their File Specs for a business card:
width - 3.625 inches
Height - 2.124 inches
@ 355 PPI or DPI
CMYK
1/8 inch Bleed/CUT
This is the size of my uploaded file samples

I will have the card printed on a 18 pt card stock - 4 color - 2 sides - with a matte coating

Tech Info: SIDE 01
For name DORIAN VALEK : font choice is FoglihtenNo07 - size 14.4 - VA 150 - Text Height 140% - text width 130% - underlined - color is 30 - 30- 30 or (1e1e1e)
For word PHOTOGRAPHY : font choice is FoglihtenNo07 - size 6.4 - VA 360 - Text Height 200% - text width 270% - underlined - color is 162-162-162 or (a2a2a2)
For DOTS - font choice is FoglihtenNo07 - size 6.73 - VA 180 - Text Height 100% - text width 163% - color is 100-179-204 or (64b3cc) - blue dots / 1-1-1 or (010101) - Black dots
For DORI@DVALEKSTUDIO.EXAMPLE - font choice is Helvetica Neue Light - size 4.55 - VA 121 - Text Height 200% - text width 132% - color is 1-1-1 or (010101)
For 555.418.2736 - font choice is Helvetica Neue Light - size 4.55 - VA 270 - Text Height 180% - text width 189% - color is 1-1-1 or (010101)
For DVALEKSTUDIO.EXAMPLE - font choice is Helvetica Neue Light - size 9.1 - VA 180 - Text Height 150% - text width 130% - color is 133-192-214 or (85c0d6)

Tech Info: SIDE 02
not certain if it is my website address - DVALEKSTUDIO.EXAMPLE - like the sample or
or my Logo with dots DORIAN VALEK PHOTOGRAPHY, WITH UNDERLINEs AND DOTS JUST LIKE FIRST SIDE - MAYBE BIGGER
the name in Helvetica Neue Light - 255 pure white -
Dots are same colors as first side
The background color of choice - at least for now issssss: 84-91-99 or (545b63)

If you think you can make my card really say Wow! Please let me know. Thank you very much!

Target Market(s)

Ad Agencies

Industry/Entity Type

Professional Photography

Contact Information for Business Card

width - 3.625 inches
Height - 2.124 inches
@ 355 PPI or DPI
CMYK
1/8 inch Bleed/CUT

Tech Info: SIDE 01

Tech Info: SIDE 02

Font styles to use
Other font styles liked:
• FoglihtenNo07 and Helvetica Neue Light

Requirements
Must have
• I am a photographer in Philadelphia, PA. I have a business card that I have designed in Photoshop. This has been an ongoing process for me for far too long. I am 85% pleased with what I have. I need some experts like yourself who has that extra 25% to make this card 110%. I use the dots throughout my website as page/topic breaks. I also use the dots on the mailing side of my direct mail pieces.
• Bramble Printworks does my printing.
• Their File Specs for a business card:
• width - 3.625 inches
• Height - 2.124 inches
• @ 355 PPI or DPI
• CMYK
• 1/8 inch Bleed/CUT
• This is the size of my uploaded file samples
• I will have the card printed on a 18 pt card stock - 4 color - 2 sides - with a matte coating
• Tech Info: SIDE 01
• For name DORIAN VALEK : font choice is FoglihtenNo07 - size 14.4 - VA 150 - Text Height 140% - text width 130% - underlined - color is 30 - 30- 30 or (1e1e1e)
• For word PHOTOGRAPHY : font choice is FoglihtenNo07 - size 6.4 - VA 360 - Text Height 200% - text width 270% - underlined - color is 162-162-162 or (a2a2a2)
• For DOTS - font choice is FoglihtenNo07 - size 6.73 - VA 180 - Text Height 100% - text width 163% - color is 100-179-204 or (64b3cc) - blue dots / 1-1-1 or (010101) - Black dots
• For DORI@DVALEKSTUDIO.EXAMPLE - font choice is Helvetica Neue Light - size 4.55 - VA 121 - Text Height 200% - text width 132% - color is 1-1-1 or (010101)
• For 555.418.2736 - font choice is Helvetica Neue Light - size 4.55 - VA 270 - Text Height 180% - text width 189% - color is 1-1-1 or (010101)
• For DVALEKSTUDIO.EXAMPLE - font choice is Helvetica Neue Light - size 9.1 - VA 180 - Text Height 150% - text width 130% - color is 133-192-214 or (85c0d6)
• Tech Info: SIDE 02
• not certain if it is my website address - DVALEKSTUDIO.EXAMPLE - like the sample or
• or my Logo with dots DORIAN VALEK PHOTOGRAPHY, WITH UNDERLINEs AND DOTS JUST LIKE FIRST SIDE - MAYBE BIGGER
• the name in Helvetica Neue Light - 255 pure white -
• Dots are same colors as first side
• The background color of choice - at least for now issssss: 84-91-99 or (545b63)
• If you think you can make my card really say Wow! Please let me know. Thank you very much!
Nice to have
• I could really use some different sizes of the dots as a Vector file?? I use Photoshop for all my designs. Thank You.
Should not have
• all listed above

```html
<!DOCTYPE html>
<html lang="en">
<head>
<meta charset="utf-8">
<title>Dorian Valek Photography – Business Card</title>
<link rel="stylesheet" href="https://fonts.googleapis.com/css2?family=Inter:wght@300&family=Playfair+Display:wght@400&display=swap">
<style>
  :root {
    --stage: #7c2a2c;
    --card-dark: #1c1c1d;
    --card-light: #fbfbfa;
    --ink: #1e1e1e;
    --ink-grey: #a2a2a2;
    --dot-blue: #64b3cc;
    --dot-dark: #010101;
    --dot-white: #f4f6f7;
    --web-blue: #85c0d6;
    --paper-white: #ffffff;
    --edge-gold: #b99a2e;
  }
  * { margin: 0; padding: 0; box-sizing: border-box; }
  html, body { width: 1200px; height: 720px; overflow: hidden; }
  body {
    background: var(--stage);
    position: relative;
    font-family: "Inter", "Helvetica Neue", Arial, sans-serif;
    font-weight: 300;
  }

  .card {
    position: absolute;
    top: 202px;
    width: 540px;
    height: 316px;
    border-bottom: 2px solid var(--edge-gold);
    box-shadow: 0 10px 24px rgba(40, 6, 8, 0.45);
  }

  /* contact side */
  .card--contact {
    left: 40px;
    background: var(--card-dark);
  }
  .pill {
    position: absolute;
    border: 1.5px solid var(--web-blue);
    border-radius: 12px;
    color: var(--paper-white);
    white-space: nowrap;
    line-height: 1;
  }
  .pill--web {
    left: 34px;
    top: 86px;
    padding: 12px 16px 11px;
    font-size: 25px;
    letter-spacing: 1px;
  }
  .pill--email {
    left: 26px;
    top: 188px;
    padding: 8px 12px 7px;
    font-size: 13px;
    letter-spacing: 0.4px;
  }
  .pill--phone {
    right: 26px;
    top: 182px;
    padding: 8px 12px 7px;
    font-size: 14px;
    letter-spacing: 3.5px;
  }
  .dot-rule {
    position: absolute;
    display: block;
  }
  .card--contact .dot-rule { left: 22px; top: 158px; }

  /* brand side */
  .card--brand {
    left: 620px;
    background: var(--card-light);
  }
  .brand {
    position: absolute;
    left: 58px;
    top: 92px;
    width: 424px;
    color: var(--ink);
    font-family: "Playfair Display", "Didot", Georgia, serif;
    font-weight: 400;
  }
  .brand__name {
    display: block;
    text-align: right;
    font-size: 46px;
    line-height: 1;
    letter-spacing: 1px;
    padding-bottom: 4px;
    border-bottom: 1.5px solid var(--ink);
  }
  .brand__trade {
    display: block;
    text-align: left;
    font-size: 20px;
    line-height: 1;
    letter-spacing: 19px;
    padding: 8px 0 5px;
    border-bottom: 1px solid var(--ink-grey);
  }
  .card--brand .dot-rule { left: 58px; top: 222px; }
</style>
</head>
<body>

  <section class="card card--contact" aria-label="Contact side">
    <p class="pill pill--web">DVALEKSTUDIO.EXAMPLE</p>

    <svg class="dot-rule" width="496" height="10" viewBox="0 0 496 10" aria-hidden="true">
      <defs>
        <pattern id="dots-light" width="24" height="10" patternUnits="userSpaceOnUse">
          <circle cx="6" cy="5" r="2.8" fill="var(--dot-white)"/>
          <circle cx="18" cy="5" r="2.8" fill="var(--dot-blue)"/>
        </pattern>
      </defs>
      <polygon points="0,5 6,2 6,8" fill="var(--dot-white)"/>
      <rect x="8" y="0" width="480" height="10" fill="url(#dots-light)"/>
      <polygon points="496,5 490,2 490,8" fill="var(--dot-blue)"/>
    </svg>

    <p class="pill pill--email">DORI@DVALEKSTUDIO.EXAMPLE</p>
    <p class="pill pill--phone">555.418.2736</p>
  </section>

  <section class="card card--brand" aria-label="Name side">
    <h1 class="brand">
      <span class="brand__name">DORIAN VALEK</span>
      <span class="brand__trade">PHOTOGRAPHY</span>
    </h1>

    <svg class="dot-rule" width="424" height="10" viewBox="0 0 424 10" aria-hidden="true">
      <defs>
        <pattern id="dots-ink" width="24" height="10" patternUnits="userSpaceOnUse">
          <circle cx="6" cy="5" r="2.8" fill="var(--dot-dark)"/>
          <circle cx="18" cy="5" r="2.8" fill="var(--dot-blue)"/>
        </pattern>
      </defs>
      <polygon points="0,5 6,2 6,8" fill="var(--dot-dark)"/>
      <rect x="8" y="0" width="408" height="10" fill="url(#dots-ink)"/>
      <polygon points="424,5 418,2 418,8" fill="var(--dot-blue)"/>
    </svg>
  </section>

</body>
</html>
```